Career Launch DL brochure

I need a design for a double sided card and 6 page flyer to hand out to students to promote our Corvane Career Launch Program. It is an 8 week program that gives budding Accountants exposure to real-life case studies in Bookkeeping & Accounting. The design for the business cards we give students at completion of the program is done. I would like some DL cards and a 6 page brochure to match the business card design. I want a template so I can just add the text I need. I have attached a sample 6 page brochure I use for employers and the business cards we use for students (2 different markets). Make sure your design matches the look of the business cards.
Updates

Reason: So far I only have one designer and I need a few more. I would prefer to work with a designer who has looked at the business card that I uploaded and come up with a design which incorporates the colours, the look and feel. Once this is agreed, the DL brochure can be done quickly I would imagine. The DL card will have very little text and will be more about design with a short message, It will be used as a Mail Out to send out in the mail to capture interest in the program.

I have extended the deadline by 24 hours due to the lack of responses. If you intend making a submission but cannot meet the deadline, please let me know at mirethd@corvanebk.com.au I am looking for a good design which matches our business card (uploaded in the brief), please do not just put all the photos at the top of every page and leave the text in a boring font with little thought to the layout. I am looking for something different. That is why I have not gone to a printer who will just dump my text straight into someone elses template. If I find a designer with a bit of spark, I am happy to guide you through until it is right. Due to the time restrictions now, I will close the applications once I find the right designer. I don't want 10 designers, I only want 1 or 2 good ones and I happy to pay a fee for second prize, or work with them exclusively on another project. The colours are already there, this should be a fairly straight forward job. I think also, the business cards are very bold, the brochure should be less bold but still be obvious that it follows the same design.

Target Market(s)

Accounting Graduates currently studying and those employed but working in non-financial jobs. Looking for work experience so they can get their foot in the door.

Industry/Entity Type

Business

Requirements
Must have
• Matching design to the attached business cards. Must be creative. Include both DL and brochure layout.
Should not have
• The attached brochure is a sample of our Employer brochure, this should be different to the student brochure in this new design.

```html
<!DOCTYPE html>
<html lang="en">
<head>
<meta charset="utf-8">
<title>Corvane Career Launch – DL Brochure</title>
<link rel="stylesheet" href="https://fonts.googleapis.com/css2?family=Lato:wght@300;400;700;900&display=swap">
<style>
  :root {
    --navy: #0d4a75;
    --navy-deep: #0a3f66;
    --green: #7cc242;
    --ink: #4a4a4a;
    --white: #ffffff;
    --paper-top: #ffffff;
    --paper-bottom: #e9ebee;
  }
  * { box-sizing: border-box; margin: 0; padding: 0; }
  html, body { width: 1200px; height: 848px; overflow: hidden; background: #fff; }
  body { font-family: "Lato", Arial, sans-serif; }
  .brochure { position: relative; width: 1200px; height: 848px; overflow: hidden; }

  /* Panels */
  .panel { position: absolute; top: 0; height: 848px; }
  .panel--inside { left: 0; width: 400px; background: linear-gradient(180deg, var(--paper-top) 0%, var(--paper-bottom) 100%); }
  .panel--back { left: 400px; width: 400px; background: var(--navy); }
  .panel--cover { left: 800px; width: 400px; background: var(--navy); }

  /* Inside panel */
  .section-tab {
    position: absolute; left: 0; width: 371px; height: 42px;
    border-radius: 0 14px 14px 0;
    color: var(--white); font-weight: 700; font-size: 14px;
    line-height: 42px; padding-left: 14px; letter-spacing: 0.1px;
  }
  .section-tab--green { background: var(--green); }
  .section-tab--navy { background: var(--navy); }
  .body-copy {
    position: absolute; left: 13px; width: 346px;
    font-size: 13px; line-height: 20px; color: var(--ink); font-weight: 400;
    text-align: justify;
  }
  .bullet-list { position: absolute; left: 13px; list-style: none; font-size: 13px; color: var(--ink); }
  .bullet-list li { line-height: 21px; }
  .bullet-list li::before { content: "• "; color: var(--green); }

  .wordmark { font-family: "Lato", Arial, sans-serif; font-weight: 700; white-space: nowrap; display: flex; align-items: center; }
  .wordmark__square { display: inline-block; flex: none; background: var(--green); }
  .wordmark--inside { position: absolute; left: 40px; top: 752px; font-size: 25px; color: var(--navy); }
  .wordmark--inside .wordmark__square { width: 26px; height: 26px; margin-right: 10px; }

  /* Back panel */
  .wordmark--back { position: absolute; left: 0; width: 400px; top: 296px; justify-content: center; font-size: 27px; color: var(--white); }
  .wordmark--back .wordmark__square { width: 26px; height: 26px; margin-right: 10px; }
  .contact { position: absolute; left: 0; width: 400px; top: 614px; text-align: center; color: var(--white); font-size: 16px; line-height: 26px; font-weight: 300; font-style: normal; }
  .contact strong { font-weight: 700; }
  .web-band { position: absolute; left: 1px; width: 398px; top: 788px; height: 43px; background: var(--green); color: var(--white); font-weight: 700; font-size: 21px; line-height: 43px; text-align: center; }

  /* Cover panel */
  .cover-accent { position: absolute; left: 1137px; top: 13px; }
  .photo-group { position: absolute; left: 802px; top: 13px; width: 374px; height: 588px; border-radius: 0 26px 18px 0; background: linear-gradient(160deg, #cfd4d8 0%, #a9b3bd 45%, #6f7f90 100%); }
  .photo-presenter { position: absolute; left: 800px; top: 562px; width: 116px; height: 286px; background: linear-gradient(180deg, #5d6b78 0%, #1f2a35 100%); border-radius: 40px 40px 0 0; }
  .headline { position: absolute; right: 18px; top: 608px; text-align: right; font-weight: 900; font-size: 31px; line-height: 30px; color: var(--white); letter-spacing: -0.2px; }
  .headline .accent { color: var(--green); }
  .logo-plate { position: absolute; left: 945px; top: 744px; width: 255px; height: 63px; background: var(--white); border-radius: 14px 0 0 14px; display: flex; align-items: center; justify-content: center; }
  .wordmark--cover { font-size: 17px; color: var(--navy); }
  .wordmark--cover .wordmark__square { width: 17px; height: 17px; margin-right: 7px; }
  .cover-web { position: absolute; right: 18px; top: 819px; color: var(--white); font-weight: 700; font-size: 14px; }
</style>
</head>
<body>
<main class="brochure">

  <section class="panel panel--inside">
    <h2 class="section-tab section-tab--green" style="top:30px">VIVAMUS MASSA MASSA, TEMPOR ET LEO EGET</h2>
    <p class="body-copy" style="top:84px; text-align:left">Sodales tellus, et imperdiet lorem viverra sit amet. Morbi convallis vitae nunc et tempus.</p>
    <ul class="bullet-list" style="top:140px">
      <li>Quisque accumsan metus nunc</li>
      <li>Laculis blandit arcu suscipit nec</li>
      <li>Sed rutrum libero non</li>
      <li>Vitae nunc et tempus.</li>
      <li>Lorem viverra sit amet.</li>
    </ul>

    <h2 class="section-tab section-tab--navy" style="top:297px">VIVAMUS MASSA MASSA, TEMPOR ET LEO EGET</h2>
    <p class="body-copy" style="top:351px">Etiam ultrices sodales tellus, et imperdiet lorem viverra sit amet. Morbi convallis vitae nunc et tempus. Quisque accumsan metus nunc.</p>

    <h2 class="section-tab section-tab--green" style="top:458px">VIVAMUS MASSA MASSA, TEMPOR ET LEO EGET</h2>
    <p class="body-copy" style="top:510px; text-align:left">Sodales tellus, et imperdiet lorem viverra sit amet. Morbi convallis vitae nunc et tempus.</p>
    <ul class="bullet-list" style="top:566px">
      <li>Quisque accumsan metus nunc</li>
      <li>Laculis blandit arcu suscipit nec</li>
      <li>Sed rutrum libero non</li>
      <li>Vitae nunc et tempus.</li>
      <li>Lorem viverra sit amet.</li>
    </ul>

    <div class="wordmark wordmark--inside"><span class="wordmark__square"></span>Corvane Career Launch</div>
  </section>

  <section class="panel panel--back">
    <div class="wordmark wordmark--back"><span class="wordmark__square"></span>Corvane Career Launch</div>
    <address class="contact">
      <strong>Address:</strong><br>
      Level 2 / 14 Harlow Lane, Marden NSW 2031<br>
      <strong>Ph</strong>: +61 2 9555 0142<br>
      <strong>Fx</strong>: +61 2 9555 0187<br>
      <strong>Email</strong>: info@CorvaneCareerLaunch.com.au
    </address>
    <div class="web-band">www.CorvaneCareerLaunch.com.au</div>
  </section>

  <section class="panel panel--cover"></section>
  <svg class="cover-accent" width="63" height="560" viewBox="0 0 63 560" aria-hidden="true">
    <path d="M8 0 H63 V560 C40 420 22 200 0 40 C0 15 2 0 8 0 Z" fill="var(--green)"/>
  </svg>
  <div class="photo-group" role="img" aria-label="Photo of a group of smiling students holding books in a school corridor"></div>
  <div class="photo-presenter" role="img" aria-label="Photo of a smiling young man in a suit pointing towards the headline"></div>
  <h1 class="headline">LOREM IPSUM<br><span class="accent">DOLOR SIT AMET</span><br>CONSECTETUR<br>ADIPISCING ELIT.</h1>
  <div class="logo-plate"><div class="wordmark wordmark--cover"><span class="wordmark__square"></span>Corvane Career Launch</div></div>
  <div class="cover-web">www.CorvaneCareerLaunch.com.au</div>

</main>
</body>
</html>
```